Business Card Design for Occupational Medicine Start Up Company

We need to design a professional business card. We are a healthcare company providing occupational medicine services to blue collar industries. We are professional, efficient and high quality service providers.

Target Market(s)

Blue Collar Industry: Shipbuilding, Ports, Trucking Companies; The Executives and Safety Officers for these companies

Industry/Entity Type

Healthcare

Contact Information for Business Card

Logo, Name, Title, Email, Phone

Other font styles liked:
• Please match our Brand Guide

Requirements
Must have
• Our Company Colors and Logo

```html
<!DOCTYPE html>
<html lang="en">
<head>
<meta charset="utf-8">
<title>Crewline Clinics – Business Card</title>
<link rel="stylesheet" href="https://fonts.googleapis.com/css2?family=Montserrat:wght@500;600;700&display=swap">
<style>
  :root {
    --bg: #d3d3d3;
    --orange: #e0a24b;
    --navy: #262f73;
    --paper: #eeeeee;
    --sky: #2299d0;
    --white: #ffffff;
  }
  html, body {
    margin: 0;
    padding: 0;
    width: 1200px;
    height: 1101px;
    overflow: hidden;
    background: var(--bg);
    font-family: "Montserrat", sans-serif;
  }
  .canvas {
    position: relative;
    width: 1200px;
    height: 1101px;
  }
  .card {
    position: absolute;
    width: 302px;
    height: 534px;
    display: block;
  }
  .card--front { left: 246px; top: 266px; }
  .card--back  { left: 641px; top: 264px; }
  .card text { font-family: "Montserrat", sans-serif; }
  .holder-name { font-size: 46px; font-weight: 700; fill: var(--navy); }
  .holder-title { font-size: 24px; font-weight: 600; fill: var(--navy); letter-spacing: 0.5px; }
  .contact-line { font-size: 16.5px; font-weight: 600; fill: var(--white); letter-spacing: 0.5px; }
  .contact-line--phone { font-size: 19px; }
  .brand-name { font-size: 38px; font-weight: 700; fill: var(--white); letter-spacing: 0.5px; }
  .brand-sub { font-size: 19px; font-weight: 500; fill: var(--white); letter-spacing: 8px; }
</style>
</head>
<body>
<main class="canvas">

  <!-- Front: holder details -->
  <svg class="card card--front" viewBox="0 0 412 727" aria-label="Business card front">
    <rect class="card-base" width="412" height="727" fill="var(--orange)"/>
    <polygon class="card-field-light" points="0,320 297,320 0,727" fill="var(--paper)"/>
    <polygon class="card-field-dark" points="412,163 412,727 0,727" fill="var(--navy)"/>

    <text class="holder-name" x="206" y="147" text-anchor="middle">JOHN DOE</text>
    <text class="holder-title" x="206" y="179" text-anchor="middle">DIRECTOR</text>

    <g class="contact-icons">
      <g class="icon icon--phone" transform="translate(259 546)">
        <circle r="16" fill="var(--paper)"/>
        <path d="M-5 -9 q-4 2 -2 9 q3 8 9 9 q3 0 4 -3 l-4 -3 l-2 2 q-3 -2 -4 -6 l2 -2 z" fill="var(--sky)"/>
      </g>
      <g class="icon icon--mail" transform="translate(307 546)">
        <circle r="16" fill="var(--paper)"/>
        <rect x="-9" y="-6" width="18" height="12" rx="1" fill="var(--orange)"/>
        <path d="M-9 -6 L0 1 L9 -6" fill="none" stroke="var(--paper)" stroke-width="1.5"/>
      </g>
      <g class="icon icon--web" transform="translate(355 546)">
        <circle r="16" fill="var(--paper)"/>
        <g fill="none" stroke="var(--navy)" stroke-width="1.4">
          <circle r="9"/>
          <ellipse rx="4" ry="9"/>
          <line x1="-9" y1="0" x2="9" y2="0"/>
          <line x1="-8" y1="-4.5" x2="8" y2="-4.5"/>
          <line x1="-8" y1="4.5" x2="8" y2="4.5"/>
        </g>
      </g>
    </g>

    <text class="contact-line contact-line--phone" x="373" y="605" text-anchor="end">+1 (123) 456-7890</text>
    <text class="contact-line" x="373" y="634" text-anchor="end">INFO@CREWLINEMED.COM</text>
    <text class="contact-line" x="373" y="663" text-anchor="end">WWW.CREWLINEMED.COM</text>
  </svg>

  <!-- Back: company name -->
  <svg class="card card--back" viewBox="0 0 412 727" aria-label="Business card back">
    <rect class="card-base" width="412" height="727" fill="var(--navy)"/>
    <polygon class="card-corner" points="0,0 77,0 0,107" fill="var(--orange)"/>
    <circle class="brand-dot" cx="166" cy="365" r="30" fill="var(--orange)"/>
    <text class="brand-name" transform="translate(248 365) rotate(-90)" text-anchor="middle" dominant-baseline="middle">CREWLINE</text>
    <text class="brand-sub" transform="translate(282 365) rotate(-90)" text-anchor="middle" dominant-baseline="middle">CLINICS</text>
  </svg>

</main>
</body>
</html>
```